Tovrelan Ltda

Logo design focused on: - Construction of civil works - Electrical services - Metal structures - Equipment rental Tomás Ibarra Leiva Manager tovrelan.ltda@brevomail.example 56 9 48215037 Quelitoco s / n, Sorimar, Valle Cordera

Building

Colors
33a6d7
0292cd
33b8a4
0555a3

```html
<!DOCTYPE html>
<html lang="es">
<head>
<meta charset="utf-8">
<title>Tovrelan Ltda – Tarjeta de presentación</title>
<link rel="stylesheet" href="https://fonts.googleapis.com/css2?family=Montserrat:wght@400;500;600;700&display=swap">
<style>
  :root {
    --bg: #e9edf1;
    --card: #ffffff;
    --band-blue: #0e72bb;
    --deep-blue: #0555a3;
    --teal: #33b8a4;
    --sky: #33a6d7;
    --ink: #1d1d1f;
    --muted-white: #dbeaf6;
  }
  * { margin: 0; padding: 0; box-sizing: border-box; }
  html, body {
    width: 1200px; height: 837px; overflow: hidden;
    background: var(--bg);
    font-family: "Montserrat", sans-serif;
  }
  .canvas { position: relative; width: 1200px; height: 837px; }
  .card {
    position: absolute; left: 100px; top: 128px;
    width: 1000px; height: 580px;
    background: var(--card);
    border-radius: 36px;
    overflow: hidden;
    box-shadow: 0 18px 40px rgba(0,0,0,.18);
  }
  .card-art { position: absolute; inset: 0; }
  .holder { position: absolute; left: 400px; top: 22px; color: #fff; }
  .holder-name { font-weight: 700; font-size: 36px; letter-spacing: .5px; }
  .holder-role { font-weight: 400; font-size: 18px; color: var(--muted-white); margin-top: 2px; margin-left: -20px; }
  .brand {
    position: absolute; left: 70px; top: 250px;
    display: flex; align-items: center; gap: 22px;
  }
  .brand-dot { width: 96px; height: 96px; border-radius: 50%; background: var(--deep-blue); }
  .brand-name { font-weight: 600; font-size: 46px; color: var(--deep-blue); letter-spacing: 1px; }
  .divider {
    position: absolute; left: 560px; top: 380px;
    width: 2px; height: 160px; background: var(--ink);
  }
  .contact { position: absolute; left: 592px; top: 405px; color: var(--ink); font-size: 17px; line-height: 1.55; }
  .contact-line { display: flex; align-items: center; gap: 10px; }
  .contact-line svg { width: 17px; height: 17px; fill: var(--ink); flex: none; }
  .address { margin-top: 14px; }
</style>
</head>
<body>
<div class="canvas">
  <div class="card">
    <svg class="card-art" viewBox="0 0 1000 580" preserveAspectRatio="none" aria-hidden="true">
      <path d="M0,0 H1000 V320 C850,232 650,165 430,122 C270,92 120,84 0,82 Z" fill="var(--band-blue)"/>
      <path d="M0,96 C120,99 270,107 430,138 C650,182 850,250 1000,336" fill="none" stroke="var(--teal)" stroke-width="7"/>
      <path d="M0,112 C120,115 270,124 430,156 C650,200 850,268 1000,352" fill="none" stroke="var(--teal)" stroke-width="4"/>
      <path d="M0,125 C120,128 270,138 430,170 C650,214 850,282 1000,365" fill="none" stroke="var(--sky)" stroke-width="2"/>
    </svg>

    <div class="holder">
      <div class="holder-name">Tomás Ibarra Leiva</div>
      <div class="holder-role">Gerente</div>
    </div>

    <div class="brand">
      <div class="brand-dot"></div>
      <div class="brand-name">Tovrelan Ltda</div>
    </div>

    <div class="divider"></div>

    <div class="contact">
      <div class="contact-line">
        <svg viewBox="0 0 20 20"><path d="M1,4 H19 V16 H1 Z M2,5 L10,11 L18,5" stroke="#fff" stroke-width="1.2"/></svg>
        <span>tovrelan.ltda@brevomail.example</span>
      </div>
      <div class="contact-line">
        <svg viewBox="0 0 20 20"><path d="M2,7 C2,3 18,3 18,7 L15,9 L13,7 H7 L5,9 Z M5,10 H15 L17,17 H3 Z"/></svg>
        <span>+56 9 48215037</span>
      </div>
      <div class="address">Quelitoco s/n, Sorimar,<br>Valle Cordera</div>
    </div>
  </div>
</div>
</body>
</html>
```